Meridane Haulage - Website

A clean, not cluttered informative website for our business. We specialize in the transportation of radioactive materials across North America. The site is mostly for information about our company and will not be used to attract business but will be used to attract employee's mainly drivers. Driver's are very hard to find in our area. One of the pages needs to be a job's posting page with an apply now button. Either an application can be filled out there or a resume can be uploaded which ever functionality works better. I would like a website that I can easily edit, ability to change text and photos.

Number of Pages Required

5+ page

Colors

Designer to choose colors to be used in the design.

Requirements
Must have
• Home - About - Services - Jobs - Contact pages
• A way prospective employee's can apply or upload their resume to be emailed to me
• Very clean apperance
Should not have
• I don't want it to be busy

```html
<!DOCTYPE html>
<html lang="en">
<head>
<meta charset="utf-8">
<title>Meridane Haulage — Home</title>
<link href="https://fonts.googleapis.com/css2?family=Montserrat:wght@400;500;600;700&display=swap" rel="stylesheet">
<style>
:root{
  --blue:#0d72c0;
  --blue-deep:#0b69b3;
  --ink:#2f3338;
  --text:#6b7075;
  --muted:#8a8e92;
  --line:#e3e5e8;
  --band:#f7f8f9;
  --white:#ffffff;
}
*{margin:0;padding:0;box-sizing:border-box}
html,body{width:737px;height:1200px;overflow:hidden}
body{position:relative;background:var(--white);font-family:"Montserrat",sans-serif;color:var(--text)}
.abs{position:absolute}
.accent{position:absolute;height:2px;background:var(--blue)}

/* header */
.site-header{position:absolute;left:0;top:0;width:737px;height:47px;background:var(--white);box-shadow:0 1px 3px rgba(0,0,0,.12);z-index:2}
.brand{position:absolute;left:67px;top:12px;font-weight:700;font-size:15px;color:var(--blue);letter-spacing:.5px;line-height:1}
.brand small{display:block;font-size:6.5px;letter-spacing:4.6px;color:var(--ink);margin-top:3px;font-weight:700}
.nav{position:absolute;top:20px;font-size:7px;font-weight:500;color:var(--ink)}
.nav.active{color:var(--blue)}
.btn-resume{position:absolute;left:565px;top:11px;width:104px;height:25px;background:var(--blue);color:var(--white);font-size:7px;font-weight:600;display:flex;align-items:center;justify-content:center;gap:5px}

/* hero */
.hero{position:absolute;left:0;top:47px;width:737px;height:390px;background:linear-gradient(180deg,#cfd2d4 0%,#9da2a6 35%,#6c7075 60%,#5a5d60 100%)}
.hero-panel{position:absolute;left:41px;top:114px;width:435px;height:200px;background:rgba(70,72,75,.55)}
.hero h1{position:absolute;left:67px;top:143px;font-size:28px;font-weight:500;line-height:37px;color:var(--white)}
.hero p{position:absolute;left:67px;top:225px;width:385px;font-size:7.2px;line-height:12.3px;color:var(--white);font-weight:500}
.btn{position:absolute;background:var(--blue);color:var(--white);font-size:6.6px;font-weight:600;display:flex;align-items:center;justify-content:center}
.arrow{position:absolute;top:186px}

/* welcome + jobs */
.welcome h2{position:absolute;left:67px;top:497px;font-size:22.5px;font-weight:500;line-height:31px;color:var(--ink)}
.welcome p{position:absolute;left:67px;width:222px;font-size:7.7px;line-height:11.3px}
.section-title{position:absolute;font-size:10px;font-weight:500;color:var(--ink);letter-spacing:.2px}
.jobs-box{position:absolute;left:338px;top:523px;width:332px;height:197px;border:1px solid var(--line)}
.job{position:absolute;left:0;width:100%}
.job-icon{position:absolute;left:9px;width:36px;height:36px;border:1px solid var(--line);display:flex;align-items:center;justify-content:center}
.job h3{position:absolute;left:53px;font-size:7.7px;font-weight:500;color:var(--ink)}
.job .cat{position:absolute;left:53px;font-size:6.6px;color:var(--muted)}
.job .meta{position:absolute;left:53px;font-size:6.4px;color:var(--muted)}
.job .meta b{color:var(--ink);font-weight:500}
.job .desc{position:absolute;left:53px;width:265px;font-size:6.4px;line-height:12px;color:var(--muted)}

/* info band */
.band{position:absolute;left:0;top:742px;width:737px;height:215px;background:var(--band)}
.col-art{position:absolute;top:62px;height:60px}
.col-text{position:absolute;top:142px;width:184px;font-size:7.7px;line-height:11.3px}
.more{position:absolute;top:188px;font-size:6.6px;color:var(--blue);font-weight:500}

/* clients */
.clients-title{position:absolute;left:0;width:737px;top:981px;text-align:center;font-size:15px;font-weight:500;color:var(--ink)}
.client{position:absolute;top:1033px;font-size:10px;font-weight:500;color:#8d9195;display:flex;align-items:center;gap:5px}
.client i{display:inline-block;width:14px;height:14px;border-radius:50%;background:#a9adb1}

/* footer */
.site-footer{position:absolute;left:0;top:1075px;width:737px;height:125px;background:var(--blue-deep);color:var(--white)}
.foot-h{position:absolute;top:24px;font-size:7.7px;font-weight:500}
.foot-t{position:absolute;top:40px;font-size:7.7px;line-height:12.8px;font-weight:500}
.foot-t u{text-underline-offset:2px}
.social{position:absolute;top:42px;font-size:6px;font-weight:600;display:flex;align-items:center;gap:3px}
.social i{display:inline-block;width:5px;height:5px;border-radius:50%;background:var(--white)}
.foot-rule{position:absolute;left:66px;top:84px;width:605px;height:1px;background:rgba(255,255,255,.7)}
.foot-link{position:absolute;top:97px;font-size:7.4px;font-weight:500}
</style>
</head>
<body>

<header class="site-header">
  <div class="brand">MERIDANE<small>HAULAGE</small></div>
  <span class="nav active" style="left:262px">HOME</span>
  <span class="nav" style="left:317px">ABOUT</span>
  <span class="nav" style="left:376px">SERVICES</span>
  <span class="nav" style="left:445px">JOBS</span>
  <span class="nav" style="left:496px">CONTACT</span>
  <a class="btn-resume">
    <svg width="12" height="9" viewBox="0 0 12 9" fill="none" stroke="#fff" stroke-width=".8"><path d="M0 1h8M0 4h6M0 7h4"/><circle cx="9" cy="6" r="2.4"/><path d="M9 4.8v2.4M7.8 6h2.4"/></svg>
    SUBMIT RESUME
  </a>
</header>

<section class="hero" role="img" aria-label="Photo of a flatbed truck hauling secured cylindrical containers in front of a brick facility under bare trees">
  <svg class="arrow" style="left:18px" width="12" height="18" viewBox="0 0 12 18"><path d="M10 2 3 9l7 7" stroke="#fff" stroke-width="2.5" fill="none"/></svg>
  <svg class="arrow" style="left:700px" width="12" height="18" viewBox="0 0 12 18"><path d="M2 2l7 7-7 7" stroke="#fff" stroke-width="2.5" fill="none"/></svg>
</section>
<div class="hero-panel" style="top:161px"></div>
<div class="hero" style="background:none;pointer-events:none">
  <div class="accent" style="left:67px;top:141px;width:34px"></div>
  <h1 style="top:145px">Largest network of<br>high quality road carriers.</h1>
  <p style="top:226px">Our large network of high quality road carriers enables us to offer nuclear transportation solutions for any over-the-road requirements. A diverse network of carriers, combined with our robust quality system, ensures that only the best carriers are considered to meet your specific needs.</p>
  <a class="btn" style="left:70px;top:273px;width:62px;height:25px">Learn more</a>
</div>

<section class="welcome">
  <div class="accent" style="left:67px;top:493px;width:20px"></div>
  <h2>Welcome to<br>Meridane Haulage</h2>
  <p style="top:562px">Our executives have diverse and extensive experience in all modes of transportation, supply chain processes, regulations, and quality management.</p>
  <p style="top:608px">Our approach to client support and communication is unique. Through the use of processes, our team of experts ensures the complete scope of customer service, from start to finish.</p>
  <p style="top:664px">Our infrastructure has been subject to rigorous client audits and is recognized as one of our major strengths.</p>
</section>

<section class="recent-jobs">
  <div class="accent" style="left:337px;top:493px;width:20px"></div>
  <h2 class="section-title" style="left:337px;top:499px">RECENT JOBS</h2>
  <div class="jobs-box">
    <article class="job" style="top:0">
      <div class="job-icon" style="top:12px">
        <svg width="13" height="13" viewBox="0 0 14 14" fill="none" stroke="#0d72c0" stroke-width="1.6"><circle cx="7" cy="7" r="5.6"/><path d="M1.6 6.2 5 5.4h4l3.4.8M7 8.6v4.2"/><circle cx="7" cy="7.4" r="1.2"/></svg>
      </div>
      <h3 style="top:15px">Driver Job in Ontario</h3>
      <span class="cat" style="top:31px">Transportation Services</span>
      <span class="meta" style="top:50px"><b>Sallery:</b> &#9635; $7,50,000 / P.A &nbsp;&nbsp;<b>Skills:</b> Driver</span>
      <p class="desc" style="top:66px">Lorem ipsum dolor sit amet, consectetuer adipiscing elit. Aenean commodo ligula eget dolor. Aenean massa. Cum sociis natoque.</p>
      <a class="btn" style="left:251px;top:12px;width:62px;height:25px">Apply Now</a>
    </article>
    <div class="abs" style="left:0;top:98px;width:100%;height:1px;background:var(--line)"></div>
    <article class="job" style="top:98px">
      <div class="job-icon" style="top:12px">
        <svg width="13" height="13" viewBox="0 0 14 14" fill="none" stroke="#0d72c0" stroke-width="1.6"><circle cx="7" cy="7" r="5.6"/><path d="M1.6 6.2 5 5.4h4l3.4.8M7 8.6v4.2"/><circle cx="7" cy="7.4" r="1.2"/></svg>
      </div>
      <h3 style="top:15px">Driver Job in Manitoba</h3>
      <span class="cat" style="top:31px">Transportation Services</span>
      <span class="meta" style="top:50px"><b>Sallery:</b> &#9635; $7,50,000 / P.A &nbsp;&nbsp;<b>Skills:</b> Driver</span>
      <p class="desc" style="top:66px">Lorem ipsum dolor sit amet, consectetuer adipiscing elit. Aenean commodo ligula eget dolor. Aenean massa.</p>
      <a class="btn" style="left:251px;top:12px;width:62px;height:25px">Apply Now</a>
    </article>
  </div>
</section>

<section class="band">
  <div class="accent" style="left:67px;top:36px;width:20px"></div>
  <h2 class="section-title" style="left:67px;top:41px">OUR SERVICES</h2>
  <div class="col-art" role="img" aria-label="Illustration of a gear and wrench service icon" style="left:132px;width:54px;background:linear-gradient(135deg,#3fa6dc,#1b6fb0);clip-path:polygon(50% 0,100% 25%,100% 75%,50% 100%,0 75%,0 25%)"></div>
  <p class="col-text" style="left:67px">Whether you need to ship a single domestic truckload or have a large international project, we are equipped with the knowledge, experience &amp; passion to get the</p>
  <span class="more" style="left:224px">MORE</span>

  <div class="accent" style="left:276px;top:36px;width:20px"></div>
  <h2 class="section-title" style="left:276px;top:41px">OUR COMPANY</h2>
  <div class="abs" style="left:277px;top:72px;font-size:25px;font-weight:700;color:var(--blue);line-height:1">MERIDANE</div>
  <div class="abs" style="left:278px;top:101px;font-size:10px;font-weight:700;letter-spacing:9px;color:var(--ink)">HAULAGE</div>
  <p class="col-text" style="left:276px">Established in 2004 by radioactive materials transportation experts, Meridane Haulage quickly proved itself as a leader in the safe and secure global transport of radioactive</p>
  <span class="more" style="left:434px">MORE</span>

  <div class="accent" style="left:486px;top:36px;width:20px"></div>
  <h2 class="section-title" style="left:486px;top:41px">OUR LOCATION</h2>
  <div class="col-art" role="img" aria-label="Illustration of a folded map with a red location pin" style="left:540px;width:70px;background:linear-gradient(135deg,#e9ecea,#bcd9a8 55%,#d63a3a);border-radius:4px;opacity:.85"></div>
  <p class="col-text" style="left:486px">Lorem ipsum dolor sit amet, consectetur adipisicing elit, sed do eiusmod tempor incididunt ut labore et dolore magna aliqua. Ut enim ad minim veniam.</p>
  <span class="more" style="left:644px">MORE</span>
</section>

<section class="clients">
  <h2 class="clients-title">Clients &amp; Awards</h2>
  <div class="accent" style="left:358px;top:1005px;width:21px"></div>
  <div class="client" style="left:84px"><i></i>Sixfold</div>
  <div class="client" style="left:188px">Buildwell</div>
  <div class="client" style="left:285px"><i></i>Farshore</div>
  <div class="client" style="left:377px">Everpath</div>
  <div class="client" style="left:476px"><i></i>Routeline</div>
  <div class="client" style="left:580px">Vitaline</div>
</section>

<footer class="site-footer">
  <h3 class="foot-h" style="left:66px">SAY HELLO</h3>
  <p class="foot-t" style="left:66px">Wants to get in touch? Lets boogie.<br><u>info@meridanehaulage.com</u></p>
  <h3 class="foot-h" style="left:274px">OUR OFFICE</h3>
  <p class="foot-t" style="left:274px">48 Alder Crossing, Suite 12, Tarrow, ON<br>(555) 014-2290</p>
  <span class="social" style="left:548px"><i></i>Gather</span>
  <span class="social" style="left:578px"><i></i>Chirrup</span>
  <span class="social" style="left:610px"><i></i>Linkwork</span>
  <span class="social" style="left:645px"><i></i>Snapframe</span>
  <div class="foot-rule"></div>
  <a class="foot-link" style="left:66px">Privacy Policy</a>
  <a class="foot-link" style="left:132px">Terms of Service</a>
  <a class="foot-link" style="left:204px">Work with Us</a>
  <span class="foot-link" style="left:446px">Copyright © 2019 Meridane Haulage. All Rights Reserved</span>
</footer>

</body>
</html>
```